A website for a Maltese Law Firm

Our law firm needs a website to further its business. The site should have a simple yet effective design. We would need the following sections: About us, Practice Areas, About Malta, Contact. These should be further split as follows:

About us: Our firm, Our values, What others say, Offices

Practice Areas: Crimimal, Citizenship & Residence, Harbour Passage Scheme, Criminal Defence, Civil Litigation, Arbitration and ADR, Commercial and Corporate, Media Law.

About Malta: just one section.

Contact: Just one section

We would also need a news feed at the front of the site to include latest news regarding our cases.

At the bottom we need a section for our Terms and a Privacy Statement.

Our logo is being attached.

Target Market(s)

All clients looking for legal assistance in Malta

Industry/Entity Type

Legal

Coding

Coded - Design and coding required

Number of Pages Required

1 page

Requirements
Must have
• It must be simple yet striking.

```html
<!DOCTYPE html>
<html lang="en">
<head>
<meta charset="utf-8">
<title>Delmare &amp; Sorrentin Advocates</title>
<link rel="stylesheet" href="https://fonts.googleapis.com/css2?family=Cinzel:wght@400;600;700&family=Open+Sans:ital,wght@0,400;0,600;0,700;1,700&display=swap">
<style>
:root{
  --ink:#222;
  --text:#444;
  --muted:#666;
  --brand:#2c5f9e;
  --brand-dark:#1d4478;
  --black:#0d0d0d;
  --footer:#151515;
  --panel:#f1f1f1;
  --white:#fff;
  --link:#b9b9b9;
}
*{box-sizing:border-box;margin:0;padding:0}
html,body{width:1200px;height:2848px;overflow:hidden;background:var(--white)}
body{font-family:"Open Sans",Arial,sans-serif;color:var(--text);position:relative}
.serif{font-family:"Cinzel",Georgia,serif}
section,header,nav,footer{position:absolute;left:0;width:1200px}

/* header */
.site-header{top:0;height:140px;background:var(--white)}
.brand-name{position:absolute;left:40px;top:52px;font-family:"Cinzel",Georgia,serif;font-weight:600;font-size:30px;color:var(--ink);letter-spacing:.5px}
.top-contact{position:absolute;top:54px;display:flex;align-items:center;gap:12px;font-size:15px;font-weight:600;color:#555;line-height:19px}
.top-contact svg{flex:none}
.top-contact.phones{left:676px}
.top-contact.mail{left:952px;top:63px}

/* nav */
.main-nav{top:140px;height:46px;background:var(--black);display:flex;padding-left:170px}
.main-nav a{font-family:"Cinzel",Georgia,serif;color:var(--white);text-decoration:none;font-size:16px;line-height:46px;padding:0 32px}
.main-nav a.active{background:var(--brand);padding:0 36px}
.main-nav a:nth-child(2){margin-left:0}

/* hero */
.hero{top:186px;height:498px}
.hero-photo{position:absolute;inset:0;background:linear-gradient(100deg,#233b5c 0%,#5d7fa8 35%,#c6d6e6 55%,#7391b5 75%,#1e3454 100%)}
.consult-form{position:absolute;left:734px;top:64px;width:400px;height:372px;background:rgba(20,28,40,.78);border:1px solid #8a96a6;border-radius:4px}
.consult-title{position:absolute;left:-6px;top:26px;width:412px;height:46px;background:var(--brand);color:var(--white);font-family:"Cinzel",Georgia,serif;font-weight:600;font-size:18px;text-align:center;line-height:46px}
.field{position:absolute;height:32px;background:rgba(30,60,105,.85);color:var(--white);font-size:12px;font-weight:600;padding:8px 14px}
.field.first{left:22px;top:94px;width:176px}
.field.last{left:202px;top:94px;width:176px}
.field.email{left:22px;top:134px;width:176px}
.field.phone{left:202px;top:134px;width:176px}
.field.message{left:22px;top:174px;width:356px;height:124px}
.submit-btn{position:absolute;left:98px;top:320px;width:204px;height:32px;background:var(--brand);color:var(--white);font-size:14px;font-weight:700;text-align:center;line-height:32px}

/* intro */
.intro{top:684px;height:152px;display:flex;align-items:center;justify-content:center}
.intro p{width:1100px;text-align:center;font-family:"Cinzel",Georgia,serif;font-size:17.5px;line-height:24px;color:var(--ink)}

/* practice areas */
.practice{top:836px;height:776px;overflow:hidden}
.practice-bg{position:absolute;inset:0;background:linear-gradient(180deg,#3a6aa8 0%,#2a5a98 45%,#1f4b86 100%)}
.section-title{position:absolute;left:0;width:1200px;text-align:center}
.section-title span{display:inline-block;font-family:"Cinzel",Georgia,serif;font-size:29px;padding:8px 14px;border-top:2px solid currentColor;border-bottom:2px solid currentColor}
.practice .section-title{top:46px;color:var(--white)}
.practice .section-title span{border-color:rgba(255,255,255,.8)}
.links{position:absolute;inset:0}
.tile{position:absolute;width:234px;height:150px;border:4px solid var(--white);border-radius:3px;overflow:hidden}
.tile-photo{position:absolute;inset:0}
.tile-label{position:absolute;left:0;width:100%;height:30px;background:rgba(0,0,0,.62);color:var(--white);font-family:"Cinzel",Georgia,serif;font-size:17px;text-align:center;line-height:30px}
.row-top .tile-label{top:0}
.row-bottom .tile-label{bottom:0}
.area-icon{position:absolute;width:68px;height:68px;border-radius:50%;background:#2b2b2b;border:4px solid var(--white);display:flex;align-items:center;justify-content:center}
.center-brand{position:absolute;left:418px;top:384px;width:364px;height:86px;background:var(--white);border-radius:6px;display:flex;align-items:center;justify-content:center;font-family:"Cinzel",Georgia,serif;font-weight:600;font-size:23px;color:var(--ink)}

/* about malta */
.about-malta{top:1612px;height:498px;background:var(--panel)}
.about-malta .section-title{top:50px;color:var(--ink)}
.about-malta .section-title span{font-size:27px;padding:6px 4px}
.malta-photo{position:absolute;left:70px;top:130px;width:508px;height:306px;border:6px solid var(--white);box-shadow:0 1px 5px rgba(0,0,0,.25);background:linear-gradient(180deg,#3a6fb5 0%,#8fb1d6 22%,#d9c9a2 40%,#b79e6e 52%,#5aa3b0 68%,#7fc2c6 100%)}
.malta-text{position:absolute;left:656px;top:128px;width:474px;font-size:16px;line-height:23px;color:var(--text)}
.more-btn{position:absolute;left:656px;top:322px;width:184px;height:40px;background:#2a2a2a;color:var(--white);border-radius:5px;font-size:16px;font-weight:700;text-align:center;line-height:40px}

/* testimonials */
.testimonials{top:2110px;height:360px;background:var(--white)}
.testimonials .section-title{top:54px;color:var(--ink)}
.testimonials .section-title span{font-size:27px;padding:6px 4px}
.avatar{position:absolute;left:88px;top:130px;width:138px;height:122px}
.quote-text{position:absolute;left:318px;top:194px;width:810px;font-size:14.5px;line-height:22px;color:var(--ink)}
.quote-mark{position:absolute;font-family:Georgia,serif;font-weight:700;font-size:70px;line-height:1;color:var(--ink)}
.quote-mark.open{left:262px;top:176px}
.quote-mark.close{left:672px;top:236px}
.quote-author{position:absolute;left:326px;top:294px;font-size:17px;font-style:italic;font-weight:700;color:var(--ink)}
.slider-dots{position:absolute;left:586px;top:286px;display:flex;gap:5px}
.slider-dots i{width:12px;height:12px;border-radius:50%;border:2px solid #999}

/* footer */
.site-footer{top:2470px;height:322px;background:var(--footer);color:var(--link)}
.foot-col{position:absolute;top:48px}
.foot-col h4{color:var(--white);font-size:15px;font-weight:700;margin-bottom:16px;text-transform:uppercase}
.foot-col li{list-style:none;font-size:12.5px;font-weight:700;line-height:21px;text-transform:uppercase}
.col-links{left:60px}
.col-areas{left:258px}
.col-offices{left:598px}
.office-line{display:flex;align-items:center;gap:12px;font-size:12.5px;font-weight:700;text-transform:uppercase;margin-bottom:10px}
.col-offices h4.second{margin-top:18px}
.office-mail{margin-top:26px}
.foot-brand{position:absolute;left:858px;top:138px;width:290px;text-align:center;font-family:"Cinzel",Georgia,serif;font-weight:600;font-size:22px;color:var(--white)}
.social{position:absolute;left:968px;top:184px;display:flex;gap:10px}
.social i{width:16px;height:16px;border-radius:50%;background:#999}
.copyright{position:absolute;top:2792px;left:0;width:1200px;height:56px;background:var(--brand);color:var(--white);font-size:11px;font-weight:700;text-align:center;line-height:40px;text-transform:uppercase}
</style>
</head>
<body>

<header class="site-header">
  <div class="brand-name">Delmare &amp; Sorrentin Advocates</div>
  <div class="top-contact phones">
    <svg width="30" height="30" viewBox="0 0 30 30"><circle cx="15" cy="15" r="13" fill="none" stroke="#555" stroke-width="2"/><path d="M10 8c1 0 2 3 2 4s-2 1-1 3 3 4 4 4 1-2 2-2 4 1 4 2-2 3-4 3c-5 0-10-6-10-10 0-2 2-4 3-4z" fill="#555"/></svg>
    <div>(356) 2000 1100 - Valletta<br>(356) 2000 2200 - Birkirkara</div>
  </div>
  <div class="top-contact mail">
    <svg width="30" height="30" viewBox="0 0 30 30"><circle cx="15" cy="15" r="13" fill="none" stroke="#555" stroke-width="2"/><rect x="8" y="10" width="14" height="10" fill="#2c5f9e"/><path d="M8 10l7 6 7-6" fill="none" stroke="#fff" stroke-width="1.4"/></svg>
    <div>info@delmarelaw.example</div>
  </div>
</header>

<nav class="main-nav">
  <a class="active" href="#">Home</a>
  <a href="#">About us &#9662;</a>
  <a href="#">Practice Areas &#9662;</a>
  <a href="#">About Malta</a>
  <a href="#">Contact</a>
</nav>

<section class="hero">
  <div class="hero-photo" role="img" aria-label="Boardroom with a polished table and empty leather chairs in blue light"></div>
  <form class="consult-form">
    <div class="consult-title">Send a message for free consultation</div>
    <div class="field first">First Name</div>
    <div class="field last">Last Name</div>
    <div class="field email">Email Address</div>
    <div class="field phone">Phone Number</div>
    <div class="field message">Message</div>
    <div class="submit-btn">SUBMIT</div>
  </form>
</section>

<section class="intro">
  <p>Lorem ipsum dolor sit amet, consectetuer adipiscing elit, sed diam nonummy nibh euismod tincidunt ut laoreet dolore magna aliquamerat volutpat. Ut wisi enim ad minim veniam, quis nostrud exerci tation ullamcorper suscipit lobortis nisl ut aliquip ex ea commodo consequat.</p>
</section>

<section class="practice">
  <div class="practice-bg" role="img" aria-label="City skyline with tall towers in blue tones"></div>
  <div class="section-title"><span>Practice Areas</span></div>

  <svg class="links" width="1200" height="776" viewBox="0 0 1200 776">
    <g stroke="#fff" stroke-width="2" stroke-dasharray="2 5" fill="none" opacity=".85">
      <line x1="214" y1="315" x2="440" y2="400"/>
      <line x1="471" y1="315" x2="540" y2="384"/>
      <line x1="728" y1="315" x2="660" y2="384"/>
      <line x1="986" y1="315" x2="760" y2="400"/>
      <line x1="214" y1="568" x2="440" y2="455"/>
      <line x1="471" y1="568" x2="540" y2="470"/>
      <line x1="728" y1="568" x2="660" y2="470"/>
      <line x1="986" y1="568" x2="760" y2="455"/>
    </g>
  </svg>

  <div class="row-top">
    <div class="tile" style="left:97px;top:148px"><div class="tile-photo" role="img" aria-label="Burning car at night" style="background:linear-gradient(160deg,#3a1a0a,#d65a12 50%,#f5a524 70%,#2b2b2b)"></div><div class="tile-label">Criminal</div></div>
    <div class="tile" style="left:354px;top:148px"><div class="tile-photo" role="img" aria-label="Hand holding a passport" style="background:linear-gradient(160deg,#d6d8dc,#8b95a5 50%,#2b3a55)"></div><div class="tile-label">Citizenship</div></div>
    <div class="tile" style="left:611px;top:148px"><div class="tile-photo" role="img" aria-label="Business meeting with a handshake" style="background:linear-gradient(160deg,#e8e6e0,#a8b0b8 50%,#4a5664)"></div><div class="tile-label">Harbour Passage</div></div>
    <div class="tile" style="left:869px;top:148px"><div class="tile-photo" role="img" aria-label="Handcuffed hands behind a suit" style="background:linear-gradient(160deg,#2a2a2a,#6a6a6a 50%,#b58a6c 70%,#1c1c1c)"></div><div class="tile-label">Criminal Defence</div></div>
  </div>
  <div class="row-bottom">
    <div class="tile" style="left:97px;top:564px"><div class="tile-photo" role="img" aria-label="Scales of justice and gavel" style="background:linear-gradient(160deg,#3a1f0c,#a8631e 50%,#d9a048 70%,#4a2a10)"></div><div class="tile-label">Civil Litigation</div></div>
    <div class="tile" style="left:354px;top:564px"><div class="tile-photo" role="img" aria-label="Arbitration hearing document with gavel" style="background:linear-gradient(160deg,#ece8e0,#c9bfae 50%,#6b4a2a)"></div><div class="tile-label">Arbitration &amp; ADR</div></div>
    <div class="tile" style="left:611px;top:564px"><div class="tile-photo" role="img" aria-label="Business team in a bright office" style="background:linear-gradient(160deg,#f2f2f2,#c7ccd4 50%,#3d4c66)"></div><div class="tile-label">Commercial</div></div>
    <div class="tile" style="left:869px;top:564px"><div class="tile-photo" role="img" aria-label="Hand signing a document with a pen" style="background:linear-gradient(160deg,#f4f1ea,#c8b8a0 50%,#5a4430)"></div><div class="tile-label">Media Law</div></div>
  </div>

  <div class="area-icon" style="left:180px;top:280px"><svg width="30" height="30" viewBox="0 0 30 30" fill="#fff"><rect x="13" y="5" width="4" height="16"/><rect x="7" y="21" width="16" height="4"/><circle cx="15" cy="5" r="3"/></svg></div>
  <div class="area-icon" style="left:437px;top:280px"><svg width="30" height="30" viewBox="0 0 30 30" fill="none" stroke="#fff" stroke-width="2.5"><rect x="7" y="4" width="16" height="22" rx="2"/><circle cx="15" cy="13" r="4"/></svg></div>
  <div class="area-icon" style="left:694px;top:280px"><svg width="30" height="30" viewBox="0 0 30 30" fill="none" stroke="#fff" stroke-width="3" stroke-linecap="round"><path d="M5 16l6 6 14-14"/></svg></div>
  <div class="area-icon" style="left:952px;top:280px"><svg width="30" height="30" viewBox="0 0 30 30" fill="none" stroke="#fff" stroke-width="3"><circle cx="10" cy="20" r="5"/><circle cx="20" cy="10" r="5"/></svg></div>

  <div class="area-icon" style="left:180px;top:530px"><svg width="30" height="30" viewBox="0 0 30 30" fill="none" stroke="#fff" stroke-width="2"><line x1="15" y1="4" x2="15" y2="26"/><line x1="6" y1="8" x2="24" y2="8"/><path d="M3 17l3-9 3 9z M21 17l3-9 3 9z" fill="#fff"/></svg></div>
  <div class="area-icon" style="left:437px;top:530px"><svg width="30" height="30" viewBox="0 0 30 30" fill="#fff"><rect x="5" y="8" width="12" height="6" transform="rotate(-35 11 11)"/><rect x="12" y="14" width="4" height="13" transform="rotate(-35 14 20)"/><rect x="4" y="24" width="14" height="3"/></svg></div>
  <div class="area-icon" style="left:694px;top:530px"><svg width="30" height="30" viewBox="0 0 30 30" fill="#fff"><rect x="8" y="5" width="14" height="21"/><g fill="#2b2b2b"><rect x="11" y="8" width="3" height="3"/><rect x="16" y="8" width="3" height="3"/><rect x="11" y="14" width="3" height="3"/><rect x="16" y="14" width="3" height="3"/><rect x="13" y="20" width="4" height="6"/></g></svg></div>
  <div class="area-icon" style="left:952px;top:530px"><svg width="30" height="30" viewBox="0 0 30 30" fill="none" stroke="#fff" stroke-width="2"><rect x="6" y="5" width="18" height="20"/><line x1="9" y1="10" x2="21" y2="10"/><line x1="9" y1="15" x2="21" y2="15"/><line x1="9" y1="20" x2="17" y2="20"/></svg></div>

  <div class="center-brand">Delmare &amp; Sorrentin</div>
</section>

<section class="about-malta">
  <div class="section-title"><span>About Malta</span></div>
  <div class="malta-photo" role="img" aria-label="Maltese harbour with colourful fishing boats and a village on the shore"></div>
  <p class="malta-text">Nam liber tempor cum soluta nobis eleifend option congue nihil imperdiet doming id quod mazim placerat facer possim assum. Typi non habent claritatem insitam; est usus legentis in iis qui facit eorum claritatem. Investigationes demonstrav erunt lectores legere me lius quod ii legunt saepius. Claritas est etiam processus dynamicus, qui sequitur mutationem consuetudium lectorum.</p>
  <div class="more-btn">More about Malta</div>
</section>

<section class="testimonials">
  <div class="section-title"><span>Clients Testimonials</span></div>
  <svg class="avatar" viewBox="0 0 138 122">
    <circle cx="61" cy="61" r="57" fill="#fff" stroke="#555" stroke-width="5"/>
    <path d="M116 52l18 10-18 10z" fill="#555"/>
    <circle cx="61" cy="61" r="52" fill="#d8c9b5" role="img" aria-label="Client portrait"/>
  </svg>
  <div class="quote-mark open">&#8221;</div>
  <p class="quote-text">Lorem ipsum dolor sit amet, consectetuer adipiscing elit, sed diam nonummy nibh euismod tincidunt ut laoreet dolore magna aliquam erat volu. Wisi enim ad minim veniam, quis nostrud exerci tation ullamcorper suscipit obortis nisl ut aliquip ex ea commodo consequat.</p>
  <div class="quote-mark close">&#8221;</div>
  <div class="quote-author">Helena Marsh</div>
  <div class="slider-dots"><i></i><i></i><i></i></div>
</section>

<footer class="site-footer">
  <div class="foot-col col-links">
    <h4>Quick Links</h4>
    <ul><li>Home</li><li>About Us</li><li>Practice Areas</li><li>About Malta</li><li>Contact</li></ul>
  </div>
  <div class="foot-col col-areas">
    <h4>Practice Areas</h4>
    <ul><li>Criminal</li><li>Citizenship &amp; Residence</li><li>Harbour Passage Scheme</li><li>Criminal Defence</li><li>Civil Litigation</li><li>Arbitration &amp; ADR</li><li>Commercial &amp; Corporate</li><li>Media Law</li></ul>
  </div>
  <div class="foot-col col-offices">
    <h4>Valetta</h4>
    <div class="office-line"><svg width="20" height="20" viewBox="0 0 20 20"><circle cx="10" cy="10" r="9" fill="none" stroke="#bbb" stroke-width="1.5"/><path d="M10 4a4 4 0 014 4c0 3-4 8-4 8s-4-5-4-8a4 4 0 014-4z" fill="#bbb"/></svg>12/4, Harbour Lane</div>
    <div class="office-line"><svg width="20" height="20" viewBox="0 0 20 20"><circle cx="10" cy="10" r="9" fill="none" stroke="#bbb" stroke-width="1.5"/><path d="M7 5c1 0 2 2 2 3s-1 1 0 2 2 3 3 3 1-1 2-1 2 1 2 2-1 2-3 2c-4 0-8-5-8-8 0-1 1-3 2-3z" fill="#bbb"/></svg>(356) 2000 1100</div>
    <h4 class="second">Birkirkara</h4>
    <div class="office-line"><svg width="20" height="20" viewBox="0 0 20 20"><circle cx="10" cy="10" r="9" fill="none" stroke="#bbb" stroke-width="1.5"/><path d="M10 4a4 4 0 014 4c0 3-4 8-4 8s-4-5-4-8a4 4 0 014-4z" fill="#bbb"/></svg>88, Olive Grove Road</div>
    <div class="office-line"><svg width="20" height="20" viewBox="0 0 20 20"><circle cx="10" cy="10" r="9" fill="none" stroke="#bbb" stroke-width="1.5"/><path d="M7 5c1 0 2 2 2 3s-1 1 0 2 2 3 3 3 1-1 2-1 2 1 2 2-1 2-3 2c-4 0-8-5-8-8 0-1 1-3 2-3z" fill="#bbb"/></svg>(356) 2000 2200</div>
    <div class="office-line office-mail"><svg width="20" height="20" viewBox="0 0 20 20"><circle cx="10" cy="10" r="9" fill="none" stroke="#bbb" stroke-width="1.5"/><rect x="5" y="7" width="10" height="7" fill="#bbb"/></svg><span style="text-transform:none">info@delmarelaw.example</span></div>
  </div>
  <div class="foot-brand">Delmare &amp; Sorrentin</div>
  <div class="social"><i></i><i></i><i></i></div>
</footer>
<div class="copyright">Copyright &copy; 2016 Delmare &amp; Sorrentin Advocates. All rights reserved.</div>

</body>
</html>
```